Clearwater Trial Sciences Bi-Fold Brochure

Contract Research Organization for Clinical Research Trial Management

Industry/Entity Type

Pharmaceutical

Font styles to use
Serif
Sans Serif

Colors
34a7d8
3176b5
f68d4d
faa54b

```html
<!DOCTYPE html>
<html lang="en">
<head>
<meta charset="utf-8">
<title>Clearwater Trial Sciences Brochure</title>
<link href="https://fonts.googleapis.com/css2?family=Montserrat:wght@500;700;800&family=Open+Sans:wght@400;600;700&family=Merriweather:wght@700&display=swap" rel="stylesheet">
<style>
  :root{
    --navy:#123a6b;
    --navy-deep:#0d2c55;
    --blue:#3176b5;
    --sky:#34a7d8;
    --orange:#f68d4d;
    --amber:#faa54b;
    --white:#ffffff;
    --ink:#243447;
    --page:#e9ebee;
  }
  *{margin:0;padding:0;box-sizing:border-box}
  html,body{width:837px;height:1200px;overflow:hidden;background:var(--page)}
  body{font-family:"Open Sans",Arial,sans-serif;color:var(--ink)}
  .spread{position:absolute;left:0;top:300px;width:837px;height:600px;display:flex;box-shadow:0 6px 18px rgba(0,0,0,.18)}
  .panel{position:relative;width:279px;height:600px;overflow:hidden}
  .panel svg.shapes{position:absolute;inset:0}

  /* About panel */
  .about{background:var(--navy);color:var(--white)}
  .about .tab{position:absolute;right:0;top:18px;background:var(--orange);padding:7px 16px 7px 26px;font-family:"Montserrat",sans-serif;font-weight:800;font-size:15px;letter-spacing:.5px;clip-path:polygon(14px 0,100% 0,100% 100%,0 100%)}
  .about .copy{position:absolute;left:20px;right:20px;top:62px}
  .about h3{font-family:"Montserrat",sans-serif;font-weight:700;font-size:10.5px;color:var(--amber);letter-spacing:.6px;margin:0 0 4px;display:flex;align-items:center;gap:6px}
  .about h3::before{content:"";width:8px;height:8px;border-radius:50%;background:var(--sky)}
  .about p{font-size:8.4px;line-height:1.5;margin-bottom:12px;color:#dbe6f3}
  .about .lab-photo{position:absolute;left:0;right:0;bottom:0;height:210px;background:radial-gradient(circle at 35% 60%,#f2a04a 0,#b4561d 28%,#2a2a3e 62%,#111a2e 100%)}

  /* Contact panel */
  .contact{background:var(--white);text-align:center}
  .contact .flask-photo{position:absolute;left:79px;top:28px;width:122px;height:122px;border-radius:50%;border:5px solid var(--white);box-shadow:0 0 0 3px var(--sky);background:radial-gradient(circle at 45% 45%,#cfeaf7 0,#6fb5dd 45%,#2a6aa5 100%)}
  .contact h2{position:absolute;left:0;right:0;top:170px;font-family:"Montserrat",sans-serif;font-weight:800;font-size:14px;color:var(--blue);letter-spacing:.5px}
  .contact address{position:absolute;left:0;right:0;top:194px;font-style:normal;font-size:8.6px;line-height:1.55;color:var(--ink)}
  .contact .socials{position:absolute;left:0;right:0;top:268px;display:flex;justify-content:center;gap:7px}
  .contact .socials span{width:15px;height:15px;border-radius:50%;background:var(--blue)}
  .contact .hours-label{position:absolute;left:0;right:0;top:300px;font-family:"Montserrat",sans-serif;font-weight:800;font-size:10.5px;color:var(--orange)}
  .contact .hours{position:absolute;left:0;right:0;top:316px;font-family:"Montserrat",sans-serif;font-weight:700;font-size:9.5px;color:var(--navy)}
  .contact .reach{position:absolute;left:0;right:0;top:470px;font-size:8.4px;color:var(--white);line-height:1.6}
  .contact .reach strong{display:block;font-family:"Montserrat",sans-serif;font-weight:800;font-size:10px;color:var(--amber);margin-bottom:3px;letter-spacing:.4px}
  .contact .web{position:absolute;left:0;right:0;bottom:12px;font-size:8.6px;font-weight:700;color:var(--white)}

  /* Cover panel */
  .cover{background:var(--white)}
  .cover .scientist-photo{position:absolute;left:0;top:0;width:279px;height:340px;background:linear-gradient(160deg,#f4f6f8 0,#d7dde3 45%,#9fb4c8 100%);clip-path:polygon(0 0,100% 0,100% 88%,0 100%)}
  .cover .title{position:absolute;right:16px;top:330px;text-align:right;color:var(--white);font-family:"Montserrat",sans-serif}
  .cover .title h1{font-weight:800;font-size:16px;line-height:1.15;letter-spacing:.3px}
  .cover .title p{font-family:"Open Sans",sans-serif;font-size:7.8px;margin-top:4px}
  .cover .brand{position:absolute;left:0;right:0;top:478px;display:flex;align-items:center;justify-content:center;gap:8px}
  .cover .brand .mark{width:18px;height:18px;border-radius:50%;background:var(--orange)}
  .cover .brand span{font-family:"Montserrat",sans-serif;font-weight:800;font-size:16px;color:var(--navy)}
  .cover .web{position:absolute;left:0;right:0;bottom:9px;text-align:center;font-size:8.6px;font-weight:700;color:var(--white)}
</style>
</head>
<body>
<main class="spread">

  <section class="panel about">
    <svg class="shapes" viewBox="0 0 279 600" aria-hidden="true">
      <polygon points="0,0 70,0 0,45" fill="#ffffff"/>
    </svg>
    <div class="tab">ABOUT US</div>
    <div class="copy">
      <h3>OUR MISSION</h3>
      <p>We advance medicine by running careful, ethical clinical trials that connect sponsors, physicians and patients, delivering reliable data that helps new therapies reach the people who need them.</p>
      <h3>WHAT WE DO</h3>
      <p>Our team manages every trial phase, from site selection and patient recruitment to monitoring, data management and regulatory reporting across many medical specialties.</p>
      <h3>WHAT WE DO</h3>
      <p>We combine experienced investigators, modern facilities and clear communication so that each study runs on time, within budget and to the highest standards of quality.</p>
    </div>
    <div class="lab-photo" role="img" aria-label="Photo of a glowing orange laboratory flask"></div>
    <svg class="shapes" viewBox="0 0 279 600" aria-hidden="true">
      <polygon points="0,390 279,440 279,452 0,402" fill="var(--orange)"/>
      <polygon points="0,380 279,430 279,436 0,386" fill="var(--sky)"/>
      <polygon points="170,600 279,520 279,600" fill="var(--amber)" opacity=".9"/>
    </svg>
  </section>

  <section class="panel contact">
    <svg class="shapes" viewBox="0 0 279 600" aria-hidden="true">
      <polygon points="0,40 279,10 279,120 0,150" fill="var(--blue)" opacity=".12"/>
      <polygon points="0,110 279,70 279,82 0,122" fill="var(--sky)"/>
      <polygon points="0,455 279,440 279,600 0,600" fill="var(--navy-deep)"/>
      <polygon points="0,446 279,430 279,440 0,456" fill="var(--orange)"/>
      <rect x="0" y="578" width="279" height="22" fill="var(--blue)"/>
    </svg>
    <div class="flask-photo" role="img" aria-label="Photo of a blue liquid in a laboratory flask"></div>
    <h2>OUR LOCATION</h2>
    <address>
      2140 Harbor Lane Suite 300<br>
      Bayview, FL, USA<br>
      1-800-555-0142<br>
      info@clearwatertrials.com<br>
      www.clearwatertrials.com
    </address>
    <div class="socials" aria-hidden="true"><span></span><span></span><span></span><span></span></div>
    <div class="hours-label">WE ARE OPEN</div>
    <div class="hours">MONDAY-FRIDAY 9:00AM-5:00PM</div>
    <div class="reach">
      <strong>FEEL FREE TO REACH US</strong>
      TELEPHONE: 1-800-555-0142<br>
      FACSIMILE: 1-800-555-0199
    </div>
    <div class="web">www.clearwatertrials.com</div>
  </section>

  <section class="panel cover">
    <div class="scientist-photo" role="img" aria-label="Photo of a scientist in a lab coat working with test tubes"></div>
    <svg class="shapes" viewBox="0 0 279 600" aria-hidden="true">
      <polygon points="0,300 279,250 279,262 0,312" fill="var(--sky)"/>
      <polygon points="0,330 279,290 279,400 0,440" fill="var(--orange)"/>
      <polygon points="0,440 279,400 279,408 0,448" fill="var(--navy)"/>
      <rect x="0" y="578" width="279" height="22" fill="var(--navy)"/>
    </svg>
    <div class="title">
      <h1>MULTISPECIALTY<br>CLINICAL RESEARCH</h1>
      <p>Trusted partner for clinical trial management</p>
    </div>
    <div class="brand">
      <div class="mark"></div>
      <span>Clearwater Trial Sciences</span>
    </div>
    <div class="web">www.clearwatertrials.com</div>
  </section>

</main>
</body>
</html>
```